Education Offering Flyer

Design a simple and clean A4 flyer, front and back, that presents our sales offering in an attractive way. The flyer consists of a title, a sub-heading, bullet points, paragraphed content and a small diagram with a caption.The design needs to be consistent with the style of the PowerPoint presentation that is attached.

We are a company that provides education software solutions for districts, schools, teachers, and students. We have a portfolio of products and services. Our offerings combine our products and services in different ways to address different education needs.

The target audience of this flyer is a decision-maker in an education organization.

Specifications:

Design a double-sided A4 flyer
Maintain our corporate logo color theme and tones (orange, blue, green, white, grey)
Follow PPTX style/theme (fonts, circles, squares, boxes)
Deliver a professional (business), clean, and modern look
Use photos that are relevant e.g. school and students with devices and technology [Optional]
Include icons [Optional]

I would like to receive the final file as a PSD format for hard copy printing. But for the purpose of review, a JPEG would be suitable.

Industry/Entity Type

Education

```html
<!DOCTYPE html>
<html lang="en">
<head>
<meta charset="utf-8">
<title>Brightpath Learning – Education Offering Flyer</title>
<link href="https://fonts.googleapis.com/css2?family=Teko:wght@500&family=Lato:wght@400;700;900&display=swap" rel="stylesheet">
<style>
  :root{
    --blue:#2f4fc4;
    --blue-deep:#2440a8;
    --green:#3aaa35;
    --orange:#f7941d;
    --yellow:#f4ee3a;
    --white:#ffffff;
    --ink:#1a1a1a;
    --backdrop:#2e2e2e;
  }
  *{box-sizing:border-box;margin:0;padding:0}
  html,body{width:945px;height:1200px;overflow:hidden;background:var(--backdrop)}
  .flyer{position:absolute;left:52px;top:10px;width:840px;height:1180px;background:var(--white);overflow:hidden;font-family:"Lato",sans-serif}
  .layer{position:absolute;left:0;top:0;width:840px;height:1180px}
  .hero-photo{position:absolute;left:0;top:0;width:840px;height:520px;
    background:linear-gradient(160deg,#8dbb3c 0%,#5f9a2a 45%,#9fc25a 100%)}
  .group-photo{position:absolute;left:411px;top:830px;width:429px;height:280px;
    background:linear-gradient(180deg,#3a5fd0 0%,#6a7fb8 45%,#4a5a80 100%)}
  .brand{position:absolute;left:640px;top:30px;width:175px;text-align:center}
  .brand-dot{width:46px;height:46px;border-radius:50%;background:var(--green);margin:0 auto 8px}
  .brand-name{font-family:"Lato",sans-serif;font-weight:700;font-size:20px;color:var(--green);line-height:1.1}
  .heading{font-family:"Teko",sans-serif;font-weight:500;color:var(--yellow);text-transform:uppercase;line-height:1;white-space:nowrap}

  .offer{position:absolute;left:366px;top:540px;width:446px;text-align:right;color:var(--white)}
  .offer .heading{font-size:32px}
  .offer p{font-size:16px;line-height:1.28;margin-top:4px}
  .offer .heading + p{margin-top:0}
  .offer .sub{margin-top:14px}
  .offer .gap{margin-top:14px}

  .card{position:absolute;left:34px;color:var(--white)}
  .card .heading{font-size:30px;margin-bottom:2px}
  .card p{font-size:12px;line-height:1.32}
  .wrap-circle{float:right}

  .card-order{top:574px;width:303px;height:254px;padding:16px 0 12px 18px;
    background:linear-gradient(180deg,var(--blue) 0%,var(--blue-deep) 100%);border-radius:32px 0 0 32px}
  .card-order .wrap-circle{width:110px;height:190px;shape-outside:circle(90px at 110% 82px)}

  .card-aspects{top:850px;width:300px;height:134px;padding:6px 0 8px 14px;background:var(--orange);border-radius:30px 0 0 30px}
  .card-aspects .heading{color:var(--blue-deep);font-size:28px}
  .card-aspects p{color:var(--ink);font-size:11.6px;line-height:1.24}
  .card-aspects .wrap-circle{width:80px;height:110px;shape-outside:circle(80px at 120% 14px)}

  .card-unified{top:1002px;width:291px;height:136px;padding:14px 44px 10px 16px;background:var(--green);border-radius:30px 0 0 0}

  .spine{position:absolute;left:319px;top:500px;width:8px;height:600px;background:var(--green)}
  .badge{position:absolute;border-radius:50%;box-shadow:0 0 0 5px var(--white)}
  .badge-network{left:254px;top:595px;width:158px;height:158px;border:9px solid var(--orange);
    background:radial-gradient(circle at 40% 40%,#4d8fd6 0%,#1b3c78 80%)}
  .badge-tablet{left:280px;top:790px;width:124px;height:124px;border:8px solid var(--green);
    background:linear-gradient(135deg,#e7d7c4 0%,#b89478 100%)}
  .badge-classroom{left:294px;top:972px;width:124px;height:124px;border:8px solid var(--orange);
    background:linear-gradient(135deg,#c9a987 0%,#7a5d4a 100%)}

  .contact{position:absolute;left:0;top:1124px;width:840px;display:flex;justify-content:center;align-items:center;gap:10px;
    font-weight:700;font-size:26px;color:var(--ink)}
  .contact svg{display:block}
  .contact .site{margin-right:12px}
</style>
</head>
<body>
<div class="flyer">
  <div class="hero-photo" role="img" aria-label="Photo of two students sitting on grass looking at a tablet"></div>

  <svg class="layer" viewBox="0 0 840 1180" aria-hidden="true">
    <defs>
      <linearGradient id="panel" x1="0" y1="0" x2="1" y2="1">
        <stop offset="0" stop-color="#2440a8"/>
        <stop offset="1" stop-color="#3b64d8"/>
      </linearGradient>
    </defs>
    <path d="M300,0 Q560,140 840,150 L840,0 Z" fill="#fff"/>
    <path d="M285,0 Q560,165 840,176 L840,152 Q560,142 300,0 Z" fill="#3aaa35"/>
    <path d="M0,372 Q150,478 340,512 L340,1180 L0,1180 Z" fill="#fff"/>
    <path d="M0,330 Q150,452 340,494 L340,514 Q150,480 0,374 Z" fill="#3aaa35"/>
    <path d="M354,512 Q600,470 840,456 L840,1120 L354,1120 Z" fill="url(#panel)"/>
  </svg>

  <div class="group-photo" role="img" aria-label="Photo of a group of cheering students with raised arms"></div>

  <div class="spine"></div>

  <section class="card card-order">
    <div class="wrap-circle"></div>
    <h2 class="heading">Bringing Order</h2>
    <p>So many acronyms, understanding technology can feel like so much alphabet soup. But with the right Learning Management System, alphabet soup turns into alphabetical order. Integration of student and content management systems and other tools provide a hub for students and educators to log in, track their work, and easily communicate.</p>
  </section>

  <section class="card card-aspects">
    <div class="wrap-circle"></div>
    <h2 class="heading">Aspects</h2>
    <p>Assignments, Lesson Planning, Individual Learning Plan, Gradebook, Assessments, Behavior, Attendance, Content Library, Virtual Classes, e-Portfolio, Calendar, Communication &amp; Collaboration, Parent Portal, and Administration.</p>
  </section>

  <section class="card card-unified">
    <p>A unified system for digital work exchange that provides students and teachers with a single, easy, and dependable solution to manage academic and administrative needs.</p>
  </section>

  <svg class="layer" viewBox="0 0 840 1180" aria-hidden="true">
    <path d="M300,1108 Q560,1050 840,1082 L840,1180 L300,1180 Z" fill="#fff"/>
    <path d="M0,1150 Q120,1120 300,1110 L300,1120 Q120,1130 0,1162 Z" fill="#3aaa35"/>
    <path d="M0,1162 Q420,1080 840,1104 L840,1180 L0,1180 Z" fill="#f7941d"/>
  </svg>

  <div class="brand">
    <div class="brand-dot"></div>
    <div class="brand-name">Brightpath Learning</div>
  </div>

  <section class="offer">
    <h1 class="heading">The Right Learning Management System</h1>
    <p>Managing teaching and learning workflows has never<br>been smoother with Brightpath Learning LMS.</p>
    <h2 class="heading sub">Teachers and Students</h2>
    <p>Certainly have enough to worry about without<br>having to focus on technology. Quizzes, tests,<br>grading, instruction time,<br>assignments — the list goes on.</p>
    <p class="gap">When a smooth and workable technology system is<br>in place, the focus isn’t on the technology, it’s on<br>teaching and learning.</p>
  </section>

  <div class="badge badge-network" role="img" aria-label="Photo of a hand touching a glowing network of user icons"></div>
  <div class="badge badge-tablet" role="img" aria-label="Photo of a teacher and a girl using a tablet"></div>
  <div class="badge badge-classroom" role="img" aria-label="Photo of students working at laptops in a classroom"></div>

  <div class="contact">
    <svg width="28" height="20" viewBox="0 0 28 20" aria-hidden="true">
      <rect x="1" y="1" width="26" height="18" rx="2" fill="#2440a8"/>
      <path d="M2,2 L14,11 L26,2" fill="none" stroke="#fff" stroke-width="2"/>
    </svg>
    <span class="site">www.brightpath.example</span>
    <svg width="24" height="26" viewBox="0 0 24 26" aria-hidden="true">
      <rect x="0" y="0" width="24" height="26" rx="5" fill="#2440a8"/>
      <path d="M8,5 C6,6 5,8 6,11 C8,16 11,19 15,21 C17,22 19,20 19,19 L16,16 L14,17 C12,16 10,14 9,11 L10,9 Z" fill="#fff"/>
    </svg>
    <span>555-010-2468</span>
  </div>
</div>
</body>
</html>
```